Lark Stewardship Business Card design

We need a creative business card design for our hospitality management company
We need the following information:
Our business Logo: Lark Stewardship
Name: Mira Dalvorsen
Phone number: 0468 319 542
Email: mira@larkstewardship.com.au
Address: 214/53 Pemberly Street, Carrow Heights 3148
Web: www.larkstewardship.com.au
I need the design to be a working file so that I can insert the names and numbers of the other staff members of our business.
The cards need to be 90 x 40mm
Thanks
Hospitality

```html
<!DOCTYPE html>
<html lang="en">
<head>
<meta charset="utf-8">
<title>Lark Stewardship – Business Cards</title>
<link rel="stylesheet" href="https://fonts.googleapis.com/css2?family=Roboto+Condensed:wght@700&family=Source+Sans+3:ital,wght@0,400;1,600&display=swap">
<style>
  :root {
    --stage: #5b3324;
    --paper: #ffffff;
    --orange: #f08a1c;
    --orange-deep: #e0721d;
    --amber: #f7b21d;
    --name: #d45f19;
    --ink: #2b2b2b;
    --ink-soft: #4a4a4a;
  }
  * { box-sizing: border-box; margin: 0; padding: 0; }
  html, body { width: 1200px; height: 610px; overflow: hidden; }
  body {
    position: relative;
    background: var(--stage);
    font-family: "Source Sans 3", "Helvetica Neue", Arial, sans-serif;
  }
  .card {
    position: absolute;
    width: 519px;
    height: 230px;
    background: var(--paper);
    box-shadow: 0 2px 6px rgba(0,0,0,.35);
    overflow: hidden;
  }
  .card--contact { left: 60px; top: 184px; }
  .card--brand-orange {
    left: 628px; top: 53px;
    background: radial-gradient(ellipse 70% 90% at 52% 40%, var(--amber) 0%, var(--orange) 55%, var(--orange-deep) 100%);
  }
  .card--brand-white { left: 628px; top: 320px; }

  .brand-mark {
    position: absolute;
    width: 78px; height: 78px;
    background: var(--orange);
  }
  .brand-name {
    position: absolute;
    font-family: "Roboto Condensed", "Arial Narrow", sans-serif;
    font-weight: 700;
    font-size: 27px;
    letter-spacing: -0.2px;
    line-height: 1;
    color: var(--orange);
    white-space: nowrap;
    text-transform: uppercase;
  }
  .card--contact .brand-mark { left: 96px; top: 61px; }
  .card--contact .brand-name { left: 0; width: 270px; text-align: center; top: 152px; }

  .contact-frame { position: absolute; left: 0; top: 0; }

  .contact-details {
    position: absolute;
    left: 299px; top: 64px;
    color: var(--ink-soft);
    font-size: 13px;
    line-height: 17px;
  }
  .contact-details .person {
    font-style: italic;
    font-weight: 600;
    font-size: 16px;
    color: var(--name);
    margin-bottom: 16px;
  }
  .contact-details .address { margin-bottom: 15px; }
  .contact-details li {
    list-style: none;
    display: flex;
    align-items: center;
    gap: 5px;
    height: 19px;
  }
  .contact-details svg { width: 10px; height: 10px; fill: var(--ink-soft); flex: none; }

  .brand-block { position: absolute; left: 0; width: 100%; text-align: center; }
  .brand-block .brand-mark { left: 221px; top: 45px; }
  .brand-block .brand-name { left: 0; width: 100%; top: 140px; }
  .card--brand-orange .brand-mark { background: var(--paper); }
  .card--brand-orange .brand-name { color: var(--paper); }
  .web {
    position: absolute;
    left: 0; width: 100%;
    text-align: center;
    font-size: 12.5px;
    letter-spacing: 1.4px;
  }
  .card--brand-orange .web { top: 197px; color: #fff3df; }
  .card--brand-white .web { top: 198px; color: var(--ink); }
</style>
</head>
<body>

<section class="card card--contact">
  <svg class="contact-frame" width="519" height="230" viewBox="0 0 519 230" aria-hidden="true">
    <defs>
      <linearGradient id="frameFill" x1="0" y1="1" x2="0" y2="0">
        <stop offset="0" stop-color="#fbc02a"/>
        <stop offset="1" stop-color="#ef8a1c"/>
      </linearGradient>
    </defs>
    <path d="M270 0 H340 V42 H384 V50 H332 V8 H280 V222 H380 V210 H388 V230 H270 Z" fill="url(#frameFill)"/>
    <circle cx="386" cy="45" r="9" fill="#f59c1f"/>
  </svg>

  <div class="brand-mark"></div>
  <div class="brand-name">Lark Stewardship</div>

  <div class="contact-details">
    <p class="person">Mira Dalvorsen</p>
    <p class="address">214/53 Pemberly Street,<br>Carrow Heights 3148</p>
    <ul>
      <li><svg viewBox="0 0 10 10"><path d="M2.2 0.6 3.8 2.6 2.9 3.7C3.5 5 4.9 6.4 6.3 7.1L7.4 6.2 9.4 7.8 8.4 9.4C4.6 9.4 0.6 5.4 0.6 1.6Z"/></svg>0468 319 542</li>
      <li><svg viewBox="0 0 10 10"><path d="M0.5 2H9.5V8H0.5ZM1 2.4 5 5.4 9 2.4V3L5 6 1 3Z"/></svg>mira@larkstewardship.com.au</li>
      <li><svg viewBox="0 0 10 10"><path d="M5 0.5A4.5 4.5 0 1 0 5 9.5 4.5 4.5 0 1 0 5 0.5ZM5 1.3C5.8 2 6.3 3.4 6.3 5S5.8 8 5 8.7C4.2 8 3.7 6.6 3.7 5S4.2 2 5 1.3ZM1.3 4.6H8.7V5.4H1.3Z"/></svg>www.larkstewardship.com.au</li>
    </ul>
  </div>
</section>

<section class="card card--brand-orange">
  <div class="brand-block">
    <div class="brand-mark"></div>
    <div class="brand-name">Lark Stewardship</div>
  </div>
  <p class="web">www.larkstewardship.com.au</p>
</section>

<section class="card card--brand-white">
  <div class="brand-block">
    <div class="brand-mark"></div>
    <div class="brand-name">Lark Stewardship</div>
  </div>
  <p class="web">www.larkstewardship.com.au</p>
</section>

</body>
</html>
```